Presentation Folder Cover For Plumbing Company

We need a presentation folder cover (FRONT AND BACK) for our plumbing business.

We specialise in plumbing, hot water, electrical and pipe relining.

This will be sent to clients and the contents pages will outline all of our company details and information.

The target market for this cover is Strata / Property Managers who look after unit buildings.

Target Market(s)

Strata & Property Managers. The higher end of the property market.

Industry/Entity Type

Plumbing

Font styles to use
Sans Serif

Colors
ec1f27
0355a3
ffffff
474747
c9c9c9

Requirements
Must have
• A4 Paper Size
• Inviting to clients to open the document and read on.
Nice to have
• Sleek, Professional and Stands Out.
Should not have
• Dark Background. Needs to be fresh and bright.

```html
<!DOCTYPE html>
<html lang="en">
<head>
<meta charset="utf-8">
<title>Crestline Contracting – Presentation Folder</title>
<link rel="stylesheet" href="https://fonts.googleapis.com/css2?family=Roboto:wght@400;700;900&family=Oswald:wght@400;500&display=swap">
<style>
  :root {
    --red: #ec1f27;
    --blue: #0355a3;
    --white: #ffffff;
    --ink: #474747;
    --silver: #c9c9c9;
    --paper-top: #ffffff;
    --paper-bottom: #e4e4e4;
  }
  * { margin: 0; padding: 0; box-sizing: border-box; }
  html, body { width: 1200px; height: 847px; overflow: hidden; background: #d9d9d9; }
  .folder { display: flex; width: 1200px; height: 847px; }
  .page {
    position: relative; width: 600px; height: 847px; overflow: hidden;
    background: linear-gradient(180deg, var(--paper-top) 0%, #f3f3f3 55%, var(--paper-bottom) 100%);
  }
  .page--back { border-right: 1px solid var(--silver); }
  .page svg.art { position: absolute; inset: 0; width: 600px; height: 847px; }
  .contact {
    position: absolute; left: 0; right: 0; top: 660px; text-align: center;
    font-family: 'Roboto', sans-serif; color: #1e1e1e;
  }
  .contact__phone { font-size: 34px; font-weight: 900; letter-spacing: 1px; }
  .contact__web { margin-top: 10px; font-size: 20px; font-weight: 700; }
  .contact__sep { color: var(--red); padding: 0 6px; }
  .brand {
    position: absolute; left: 250px; right: 20px; top: 90px; text-align: center;
    font-family: 'Roboto', sans-serif; color: var(--blue);
  }
  .brand__name { font-size: 40px; font-weight: 900; letter-spacing: 1px; line-height: 1.05; }
  .brand__tagline { margin-top: 14px; font-size: 16px; font-weight: 700; color: #1e1e1e; }
  .services {
    position: absolute; left: 0; right: 0; top: 605px; text-align: center;
    font-family: 'Oswald', sans-serif; text-transform: uppercase;
  }
  .services__intro { color: var(--blue); font-size: 19px; font-weight: 500; }
  .services__list { margin-top: 4px; color: #1e1e1e; font-size: 27px; font-weight: 500; letter-spacing: 0.3px; }
  .services__sep { color: var(--red); padding: 0 10px; }
</style>
</head>
<body>
<main class="folder">
  <section class="page page--back">
    <svg class="art" viewBox="0 0 600 847">
      <defs>
        <linearGradient id="tools" x1="0" y1="0" x2="1" y2="1">
          <stop offset="0" stop-color="#d9b08c"/><stop offset="0.5" stop-color="#b8504a"/><stop offset="1" stop-color="#c9c3b8"/>
        </linearGradient>
        <linearGradient id="trap" x1="0" y1="0" x2="1" y2="1">
          <stop offset="0" stop-color="#e6e6e6"/><stop offset="0.6" stop-color="#a9acb0"/><stop offset="1" stop-color="#3f5566"/>
        </linearGradient>
      </defs>
      <polygon class="band band--red" points="490,160 600,160 600,205 470,220" fill="var(--red)"/>
      <polygon role="img" aria-label="Photo of plumbing tools, valves and wrenches" points="0,250 440,230 315,580 0,600" fill="url(#tools)"/>
      <polygon role="img" aria-label="Photo of a plumber fitting a chrome sink trap" points="465,228 600,218 600,575 340,585" fill="url(#trap)"/>
      <polygon class="band band--red" points="0,612 300,598 282,648 0,662" fill="var(--red)"/>
    </svg>
    <div class="contact">
      <p class="contact__phone">00 0000 000</p>
      <p class="contact__web">uremail@web.com<span class="contact__sep">|</span>www.urweb.com</p>
    </div>
  </section>

  <section class="page page--front">
    <svg class="art" viewBox="0 0 600 847">
      <defs>
        <linearGradient id="worker" x1="0" y1="0" x2="1" y2="1">
          <stop offset="0" stop-color="#c98a6a"/><stop offset="0.45" stop-color="#3f6f8f"/><stop offset="1" stop-color="#2f4d66"/>
        </linearGradient>
      </defs>
      <polygon class="accent accent--blue" points="0,0 235,0 22,565 0,565" fill="var(--blue)"/>
      <polygon role="img" aria-label="Photo of a plumber with a tool belt holding a pipe wrench and hoses" points="172,240 600,232 600,555 52,572" fill="url(#worker)"/>
    </svg>
    <div class="brand">
      <p class="brand__name">CRESTLINE<br>CONTRACTING</p>
      <p class="brand__tagline">Plumbing • Electrical • Hot Water</p>
    </div>
    <div class="services">
      <p class="services__intro">We specialize in</p>
      <p class="services__list">Plumbing<span class="services__sep">|</span>Hot Water<span class="services__sep">|</span>Electrical<span class="services__sep">|</span>Pipe Relining</p>
    </div>
  </section>
</main>
</body>
</html>
```